Corporate New Year's card (typography)

My client, a healthcare consulting firm, will be sending out approximately 500 New Year's cards to key accounts (hospital CEOs, public health department heads, etc.). We need a look that's professional & sophisticated, while conveying a message that's warm and personal.

The design brief is attached, along with the firm's logo. As you'll see, this project is mostly about typography. I don't have a lot of preconceived notions as to how this should look; I look forward to being surprised. Print size is 5x7 inches (A7). If anything is less than clear, please ask. Thanks!

Industry/Entity Type

Healthcare

Requirements
Must have
• Just to clarify the creative brief: This is a die cut card. The "doorway" space is actually cut out of the front of the card. The secondary messaging ("Wishing you every happiness...") is on the inside of the card, along with the logo. A portion of the logo shows through the cutout -- not the whole logo, just enough to tease the recipient ("Who's this from?" "What's that on the inside?"). When submitting designs, please include BOTH the cover and the inside of the card. My client wants to get an idea of how the two parts relate, what will show through the hole, etc. Thank you!

```html
<!DOCTYPE html>
<html lang="en">
<head>
<meta charset="utf-8">
<title>New Year Card – Cover and Inside</title>
<link rel="stylesheet" href="https://fonts.googleapis.com/css2?family=Cinzel:wght@400;500&family=Great+Vibes&family=Arimo&display=swap">
<style>
  :root {
    --stage-light: #e6e8f1;
    --stage-mid: #b9bdd6;
    --stage-deep: #8e94b8;
    --cover-light: #4f78b5;
    --cover-deep: #2a4689;
    --cover-text: #ffffff;
    --quote-mark: rgba(214, 222, 240, 0.6);
    --inside-paper: #ffffff;
    --inside-ink: #233380;
    --caption-ink: #111111;
    --card-shadow: rgba(20, 24, 50, 0.55);
  }
  * { margin: 0; padding: 0; box-sizing: border-box; }
  html, body { width: 1000px; height: 1200px; overflow: hidden; }
  body {
    position: relative;
    background:
      radial-gradient(ellipse 420px 300px at 30px 560px, var(--stage-deep), transparent 70%),
      radial-gradient(ellipse 500px 420px at 900px 300px, var(--stage-light), transparent 70%),
      linear-gradient(160deg, var(--stage-mid), var(--stage-light) 55%, var(--stage-mid));
  }
  .card {
    position: absolute;
    left: 168px;
    width: 667px;
    height: 476px;
    box-shadow: 6px 8px 16px var(--card-shadow);
  }
  .card--cover {
    top: 52px;
    background: linear-gradient(30deg, var(--cover-deep) 0%, var(--cover-light) 55%, #4b70ad 100%);
  }
  .card--inside { top: 645px; background: var(--inside-paper); }

  .cover-quote {
    position: absolute;
    left: 0; width: 628px; top: 108px;
    text-align: center;
    font-family: "Cinzel", serif;
    font-size: 22px;
    line-height: 38px;
    letter-spacing: 0.6px;
    color: var(--cover-text);
    text-shadow: 0 2px 6px rgba(20, 30, 70, 0.45);
  }
  .cover-quote .initial { font-size: 27px; }
  .quote-mark {
    position: absolute;
    font-family: "Cinzel", serif;
    font-size: 78px;
    line-height: 1;
    color: var(--quote-mark);
  }
  .quote-mark--open { left: 96px; top: 92px; }
  .quote-mark--close { left: 534px; top: 168px; }
  .cover-attribution {
    position: absolute;
    left: 412px; top: 240px;
    font-family: "Great Vibes", cursive;
    font-size: 16px;
    color: var(--cover-text);
  }
  .door-cutout { position: absolute; left: 528px; top: 336px; }

  .inside-message {
    position: absolute;
    left: 0; width: 100%; top: 166px;
    text-align: center;
    font-family: "Cinzel", serif;
    font-size: 22px;
    line-height: 38px;
    letter-spacing: 0.5px;
    color: var(--inside-ink);
  }
  .inside-message .initial { font-size: 27px; }
  .brand-sign {
    position: absolute;
    left: 510px; top: 366px;
    width: 110px;
    text-align: center;
    font-family: "Cinzel", serif;
    font-size: 15px;
    font-weight: 500;
    color: var(--inside-ink);
  }
  .brand-sign__dot {
    display: block;
    width: 34px; height: 34px;
    margin: 0 auto 10px;
    border-radius: 50%;
    background: var(--inside-ink);
  }

  .caption {
    position: absolute;
    left: 172px;
    font-family: "Arimo", sans-serif;
    font-size: 27px;
    color: var(--caption-ink);
  }
</style>
</head>
<body>

  <section class="card card--cover" aria-label="Card cover">
    <span class="quote-mark quote-mark--open" aria-hidden="true">“</span>
    <p class="cover-quote">
      <span class="initial">H</span>appiness often sneaks in<br>
      through a door<br>
      you didn’t know you left open
    </p>
    <span class="quote-mark quote-mark--close" aria-hidden="true">”</span>
    <p class="cover-attribution">Jonah Bellamy</p>

    <svg class="door-cutout" width="70" height="116" viewBox="0 0 70 116" aria-label="Die-cut doorway revealing part of the inside name">
      <defs>
        <clipPath id="doorway">
          <rect x="6" y="2" width="60" height="110"/>
        </clipPath>
      </defs>
      <rect x="6" y="2" width="60" height="110" fill="#ffffff"/>
      <g clip-path="url(#doorway)" fill="#233380">
        <circle cx="44" cy="42" r="17"/>
        <text x="34" y="92" font-family="Cinzel, serif" font-size="15" font-weight="500">LWE</text>
      </g>
      <polygon points="2,6 22,2 22,112 2,108" fill="#ffffff" stroke="#c9d2e6" stroke-width="1"/>
      <circle cx="6" cy="58" r="1.6" fill="#4f78b5"/>
    </svg>
  </section>

  <p class="caption" style="top:541px;">Front</p>
  <p class="caption" style="top:582px;">Die-Cut Door Space showing portion of the logo</p>

  <section class="card card--inside" aria-label="Card inside">
    <p class="inside-message">
      <span class="initial">W</span>ishing you every happiness<br>
      as you open the door on 2015.
    </p>
    <div class="brand-sign">
      <span class="brand-sign__dot" aria-hidden="true"></span>
      Clearwell
    </div>
  </section>

  <p class="caption" style="top:1137px;">Inside</p>

</body>
</html>
```